We are in search of a new business card design for our business. We have a Mexican Grocery Store called Tortilla Grove Market, we would like to see that some have mexican design, but we are open to any type of designs.

Phone: to be announced
Fax: to be announced

Address is:
2415 Calloway Blvd
Harwick, PA 17390

```html
<!DOCTYPE html>
<html lang="en">
<head>
<meta charset="utf-8">
<title>Tortilla Grove Market – Business Card</title>
<link rel="stylesheet" href="https://fonts.googleapis.com/css2?family=Roboto:wght@400;700;900&display=swap">
<style>
  :root{
    --bg:#ecebe8;
    --card:#ffffff;
    --red:#dc3540;
    --red-dark:#b3202b;
    --yellow:#ffd21f;
    --yellow-dark:#e9a800;
    --white:#ffffff;
    --ghost:rgba(255,255,255,0.16);
  }
  html,body{margin:0;padding:0;overflow:hidden;}
  body{
    width:1200px;height:1023px;
    background:var(--bg);
    font-family:"Roboto",Arial,sans-serif;
    position:relative;
  }
  .card{
    position:absolute;left:180px;top:271px;
    width:840px;height:480px;
    background:linear-gradient(135deg,#ffffff 0%,#f1f1f1 100%);
    box-shadow:0 10px 30px rgba(0,0,0,0.18);
    overflow:hidden;
  }
  .card__panel{position:absolute;inset:0;}
  .card__ghost-name{
    position:absolute;left:600px;top:40px;
    font-weight:900;font-size:46px;line-height:1.05;
    color:var(--ghost);width:230px;
  }
  .brand{
    position:absolute;left:80px;top:300px;
    display:flex;align-items:center;gap:16px;
  }
  .brand__dot{
    width:46px;height:46px;border-radius:50%;
    background:var(--red);flex:none;
  }
  .brand__name{
    font-weight:900;font-size:34px;color:var(--red);
    letter-spacing:0.5px;white-space:nowrap;
  }
  .contact{
    position:absolute;left:585px;top:250px;
    display:flex;flex-direction:column;gap:18px;
    color:var(--white);font-size:16px;
  }
  .contact__row{display:flex;align-items:flex-start;gap:12px;}
  .contact__icon{
    width:26px;height:26px;border-radius:6px;flex:none;
    background:linear-gradient(180deg,var(--yellow),var(--yellow-dark));
    display:flex;align-items:center;justify-content:center;
  }
  .contact__address{font-weight:700;font-size:18px;line-height:1.3;}
  .contact__value{color:var(--yellow);}
</style>
</head>
<body>
  <div class="card">
    <svg class="card__panel" width="840" height="480" viewBox="0 0 840 480" aria-hidden="true">
      <defs>
        <linearGradient id="panelRed" x1="0" y1="0" x2="1" y2="1">
          <stop offset="0" stop-color="#b3202b"/>
          <stop offset="0.5" stop-color="#dc3540"/>
          <stop offset="1" stop-color="#b3202b"/>
        </linearGradient>
      </defs>
      <path d="M590 0 L840 0 L840 480 L548 480 L524 282 Q520 258 530 238 Z" fill="url(#panelRed)"/>
    </svg>

    <div class="card__ghost-name" aria-hidden="true">Tortilla Grove</div>

    <div class="brand">
      <span class="brand__dot"></span>
      <span class="brand__name">Tortilla Grove Market</span>
    </div>

    <div class="contact">
      <div class="contact__row">
        <span class="contact__icon">
          <svg width="14" height="16" viewBox="0 0 14 16"><path d="M7 0a6 6 0 0 0-6 6c0 4.5 6 10 6 10s6-5.5 6-10a6 6 0 0 0-6-6zm0 8.3A2.3 2.3 0 1 1 7 3.7a2.3 2.3 0 0 1 0 4.6z" fill="#c0262f"/></svg>
        </span>
        <div class="contact__address">2415 Calloway Blvd<br>Harwick, PA 17390</div>
      </div>
      <div class="contact__row">
        <span class="contact__icon">
          <svg width="14" height="14" viewBox="0 0 24 24"><path d="M6.6 10.8a15.1 15.1 0 0 0 6.6 6.6l2.2-2.2c.3-.3.7-.4 1-.2 1.1.4 2.300.6 3.600.6.6 0 1 .4 1 1V20c0 .6-.4 1-1 1A17 17 0 0 1 3 4c0-.6.4-1 1-1h3.5c.6 0 1 .4 1 1 0 1.3.2 2.5.6 3.6.1.3 0 .7-.2 1z" fill="#2f8f3a"/></svg>
        </span>
        <div>Phone: <span class="contact__value">0420-555-7316</span></div>
      </div>
      <div class="contact__row">
        <span class="contact__icon">
          <svg width="14" height="14" viewBox="0 0 24 24"><path d="M6 3h10l2 2v5H6z M3 10h18v9H3z M7 15h10v6H7z" fill="#c0262f"/></svg>
        </span>
        <div>Fax: <span class="contact__value">002-614-3059</span></div>
      </div>
    </div>
  </div>
</body>
</html>
```